New and upgraded www.ortavelfunds.com content & design financial markets

We need an upgrade of our site. The current site is www.ortavelfunds.com
Navigation with full site map i.e. the user can select any page from any menu item.

The “Insights” (Insikter) page will remain as is except new design AND with far more possibilities to add thumbnails, picts, videos etc. The user will have to logon to be able to read the full story.

The “Produkter & Tjänster” (“How to invest” in current web) will contain about the same info as the current “How to invest” pages.

Some pages will contain one or more videos and or speaker supported “live” graphics which we will supply. The media content shall be easy to change.

The site will have two languages from start, English and Swedish. There will be more languages added within 1 year or slightly more.

All texts will be provided by us.

I’m attaching a PDF with suggested content for some of the new pages. However this is just content and absolutely no design. We need new design for the total of the site as well as for the graphics.

Expectation info:
These sites (Both major players in our business) can be used as inspiration:
https://www.brindlemoor.com/eu/en/
https://www.tessquarry.com/index.html

Below some opt-OUT and opt-IN graphic rules in connection with the Web supporting our business acumen and brand:

Opt-OUT:
- images similar to educational comic books - it signals an authoritarian approach where the customer is small (insubstantial).
- images that signal trading, cyber, mystery and fast-paced business. We are extremely long-term and invest in real companies
- avoid images containing coins, calculators and banknotes. We're not a savings bank company. or payment service-branch
- avoid images of large data flows, because we should not make facts complex, but simple and comprehensible
- avoid sensing pictures of photo models. We are real people who stand for our efforts. We're not going to hide.
- avoid pictures of suits and tie. They signal rigid-banking. We're smart-investment, flexible, adaptable. Rather curl up your sleeves and show that we’re building something valuable.
- avoid pictures of skyscrapers and cool bank pictures - because they signal the more old valuations of big capital and giant banks - that we are not at all. I know we've had clean facades before. As long as we're not talking about bank skyscrapers, I'm in.

Opt-IN
- pictures of Anders in moderate amount - he is our symbol person
- films with Anders and explaining graphical films - explaining and clarifying
- images of pedagogy that give the customer a sense of overview and insights that we give to the customers in our service
- illustrations that explain and deepen our work
- pictures and bars that in 3d illustrate our consistent results and stable delivery
- images that signal that we have a full grasp of data, flows and analyses - without the image becoming a space adventure
- use the logo as a grid, shape and colour.
- no genre portraits, rather pictures of real customers - which gives a sense of why they are customers here
- images that support our core i.e. is science, innovation, unrestricted thinking (“out of the box” – (don’t like that sentence)), smart-solutions, data-driven, client-cantered, flexible and adaptable to client needs and expectation.
- Solid - to be trustworthy in any economic climate
- Long term - consistent work and choices. No trading. Numbers talk
- Data-driven - real tech - combining years of work in finance with straight on tech

Presenting on the webpage:
The story in text and illustration
Show the truth - we have a great history to show and give space
Only numbers and graphs that has a meaning - no artificial numbers etc.
Updates

Target Market(s)

Europe

Coding

Coded - Design and coding required

Number of Pages Required

5+ page

Colors

Designer to choose colors to be used in the design.

Requirements
Must have
• Colours in line with www.ortavelfunds.com

```html
<!DOCTYPE html>
<html lang="en">
<head>
<meta charset="utf-8">
<title>Ortavel Funds — Your Personal Investment Advisor</title>
<link href="https://fonts.googleapis.com/css2?family=Montserrat:wght@400;600;700;800&family=Open+Sans:wght@400;600&display=swap" rel="stylesheet">
<style>
:root{
  --navy:#0d1f5c;
  --royal:#173a9c;
  --blue:#1f4fc4;
  --deep:#091540;
  --ink:#1b2550;
  --text:#333a4d;
  --muted:#6b7285;
  --light:#eceef2;
  --white:#ffffff;
  --line:rgba(255,255,255,.55);
}
*{box-sizing:border-box;margin:0;padding:0}
html,body{width:1200px;height:4256px;overflow:hidden}
body{font-family:"Open Sans",Arial,sans-serif;color:var(--text);background:var(--white);position:relative}
h1,h2,h3,h4,.nav,.btn,.brand{font-family:"Montserrat",Arial,sans-serif}

/* header */
.site-header{position:absolute;top:0;left:0;width:1200px;height:60px;background:var(--white);display:flex;align-items:center;padding:0 84px;justify-content:space-between;z-index:5}
.brand{display:flex;align-items:center;gap:12px;font-weight:700;font-size:26px;color:var(--navy)}
.brand .mark{width:22px;height:22px;background:var(--navy)}
.nav{display:flex;gap:36px;font-size:12px;font-weight:600;color:var(--ink);letter-spacing:.5px}
.nav a{color:inherit;text-decoration:none;padding-bottom:6px}
.nav a.active{border-bottom:2px solid var(--navy)}

/* hero */
.hero{position:absolute;top:60px;left:0;width:1200px;height:720px;overflow:hidden}
.hero-photo{position:absolute;inset:0;background:linear-gradient(160deg,#6c92d6 0%,#b6cdec 30%,#3b5ea8 55%,#15296a 100%)}
.hero-shade{position:absolute;inset:0;background:linear-gradient(180deg,rgba(9,21,64,.1),rgba(9,21,64,.35))}
.hero-copy{position:absolute;top:200px;width:100%;text-align:center;color:var(--white)}
.hero-copy .kicker{font-family:"Montserrat",sans-serif;font-size:30px;letter-spacing:2px;font-weight:400}
.hero-copy h1{font-size:56px;line-height:60px;font-weight:800;margin-top:4px}
.btn{display:inline-block;background:var(--navy);color:var(--white);font-size:12px;font-weight:700;letter-spacing:1px;padding:12px 26px;text-decoration:none}
.btn.ghost{background:transparent;border:2px solid var(--white)}
.hero .btn{margin-top:28px}
.arrow{position:absolute;top:325px;width:50px;height:50px;border-radius:50%;background:rgba(255,255,255,.35)}
.hero-curve{position:absolute;bottom:0;left:0}

/* about */
.about{position:absolute;top:790px;width:1200px;text-align:center}
.about h2{font-size:32px;font-weight:800;color:var(--navy);margin-top:22px}
.about p{width:900px;margin:22px auto 0;font-size:15px;line-height:26px;color:var(--text)}
.emblem{width:30px;height:30px;background:var(--navy);transform:rotate(45deg);margin:0 auto}

/* diamonds */
.diamonds{position:absolute;top:1050px;left:0;width:1200px;height:460px}
.diamond{position:absolute;transform:rotate(45deg);box-shadow:0 10px 30px rgba(9,21,64,.35)}
.diamond.side{width:268px;height:268px;top:96px;background:linear-gradient(135deg,#2a2f3e,#10152a)}
.diamond.center{width:290px;height:290px;top:85px;left:455px;background:linear-gradient(135deg,var(--blue),var(--royal));border:6px solid var(--white);z-index:2}
.diamond-copy{position:absolute;text-align:center;color:var(--white);z-index:3}
.diamond-copy.side{width:150px;top:170px}
.diamond-copy.center{width:220px;left:490px;top:165px}
.diamond-copy h3{font-size:15px;font-weight:700;margin:10px 0 6px}
.diamond-copy p{font-size:11px;line-height:16px;color:rgba(255,255,255,.8)}

/* approach */
.approach{position:absolute;top:1520px;left:0;width:1200px;height:540px;background:linear-gradient(180deg,#0e2470,#163a9b);color:var(--white);text-align:center}
.approach h2{margin-top:96px;font-size:32px;font-weight:700;letter-spacing:1px}
.approach .lead{margin:22px auto 0;width:520px;font-size:15px;line-height:25px;color:rgba(255,255,255,.85)}
.pillars{position:absolute;top:260px;left:0;width:1200px}
.pillar{position:absolute;width:260px;text-align:center}
.pillar .ring{width:76px;height:76px;border:2px solid var(--white);border-radius:50%;margin:0 auto;display:flex;align-items:center;justify-content:center}
.pillar h4{margin-top:24px;font-size:14px;font-weight:700;line-height:20px}

/* intelligence */
.intelligence{position:absolute;top:2060px;left:0;width:1200px;height:520px;background:var(--light)}
.screen{position:absolute;left:140px;top:110px;width:420px;height:270px;background:linear-gradient(160deg,#e8eefb 0%,#9db4ea 45%,#2c4fb8 100%);border:10px solid #1a1d26;border-radius:8px 8px 0 0}
.screen-base{position:absolute;left:115px;top:380px;width:470px;height:14px;background:#c8ccd4;border-radius:0 0 12px 12px}
.intel-copy{position:absolute;left:660px;top:128px;width:440px}
.intel-copy h2,.advisory h2{font-size:24px;font-weight:800;color:var(--navy)}
.intel-copy p,.advisory p{font-size:14px;line-height:22px;margin-top:18px;color:var(--text)}
.intel-copy .btn,.advisory .btn{margin-top:26px}

/* split panels */
.panel{position:absolute;top:2580px;width:596px;height:480px;color:var(--white);text-align:center;overflow:hidden}
.panel.left{left:0;background:linear-gradient(160deg,#1c2f7a,#0a1a55)}
.panel.right{left:604px;background:linear-gradient(200deg,#2a468f,#0c1c5a)}
.panel-inner{position:absolute;top:160px;width:100%}
.panel h2{font-size:24px;font-weight:800;letter-spacing:.5px}
.panel p{width:380px;margin:16px auto 0;font-size:13px;line-height:20px;color:rgba(255,255,255,.85)}
.panel .btn{margin-top:24px}

/* advisory */
.advisory{position:absolute;top:3060px;left:0;width:1200px;height:500px;background:var(--white)}
.advisory-photo{position:absolute;right:0;top:0;width:640px;height:500px;background:linear-gradient(90deg,#ffffff 0%,#d9e0ec 22%,#8fa2c4 60%,#3d4f7c 100%)}
.advisory-copy{position:absolute;left:150px;top:120px;width:400px}

/* contact */
.contact{position:absolute;top:3560px;left:0;width:1200px;height:520px;background:linear-gradient(180deg,#1b3fae,#0e2677);color:var(--white)}
.contact h2{text-align:center;margin-top:82px;font-size:26px;font-weight:700;letter-spacing:1px}
.contact-form{position:absolute;left:180px;top:144px;width:840px;height:244px;border:1px solid var(--line);display:flex}
.fields{width:420px;padding:12px 24px 0 0}
.field{height:56px;border-bottom:1px solid var(--line);padding:18px 0 0 10px;font-size:13px;color:rgba(255,255,255,.85)}
.fields .field{border-right:1px solid var(--line)}
.message{flex:1;padding:16px 18px;font-size:13px;color:rgba(255,255,255,.85);border-left:1px solid var(--line)}
.contact .submit{position:absolute;left:540px;top:412px;width:120px;text-align:center;border:1px solid var(--white);background:transparent}

/* footer */
.site-footer{position:absolute;top:4080px;left:0;width:1200px;height:176px;background:var(--white);text-align:center}
.site-footer .nav{justify-content:center;gap:40px;margin-top:50px;font-size:12px}
.social{display:flex;justify-content:center;gap:10px;margin-top:28px}
.social span{width:26px;height:26px;border-radius:50%;background:var(--royal)}
.copyright{font-size:11px;color:var(--muted);margin-top:16px}
</style>
</head>
<body>

<header class="site-header">
  <div class="brand"><span class="mark"></span>Ortavel Funds</div>
  <nav class="nav">
    <a class="active" href="#">PHILOSOPHY</a><a href="#">HOW TO INVEST</a><a href="#">WHAT WE DO</a><a href="#">CONTACT</a><a href="#">INSIGHT</a>
  </nav>
</header>

<section class="hero">
  <div class="hero-photo" role="img" aria-label="Upward view of glass office towers against a bright blue sky"></div>
  <div class="hero-shade"></div>
  <div class="hero-copy">
    <div class="kicker">ORTAVEL FUNDS</div>
    <h1>YOUR PERSONAL<br>INVESTMENT ADVISOR</h1>
    <a class="btn" href="#">LEARN MORE</a>
  </div>
  <div class="arrow" style="left:112px">
    <svg width="50" height="50" viewBox="0 0 50 50"><path d="M28 17 L20 25 L28 33" fill="none" stroke="#fff" stroke-width="3"/></svg>
  </div>
  <div class="arrow" style="right:76px">
    <svg width="50" height="50" viewBox="0 0 50 50"><path d="M22 17 L30 25 L22 33" fill="none" stroke="#fff" stroke-width="3"/></svg>
  </div>
  <svg class="hero-curve" width="1200" height="110" viewBox="0 0 1200 110">
    <path d="M0 40 Q600 150 1200 40 L1200 110 L0 110 Z" fill="#173a9c"/>
    <path d="M0 60 Q600 160 1200 60 L1200 110 L0 110 Z" fill="#ffffff"/>
  </svg>
</section>

<section class="about">
  <div class="emblem"></div>
  <h2>ABOUT ORTAVEL FUNDS</h2>
  <p>We are a privately held firm dedicated to clients who have entrusted us with their wealth. We act solely and transparently in the best interest of our clients. We pride ourselves on our discretion and confidentiality. You can be assured of a totally Client-centric service, high quality, totally unbiased, investment advice.</p>
</section>

<section class="diamonds">
  <div class="diamond side" style="left:226px" role="img" aria-label="Dark photo of an office meeting"></div>
  <div class="diamond side" style="left:706px" role="img" aria-label="Dark photo of a client conversation"></div>
  <div class="diamond center"></div>

  <div class="diamond-copy side" style="left:230px">
    <svg width="32" height="32" viewBox="0 0 36 36"><circle cx="18" cy="18" r="15" fill="none" stroke="#fff" stroke-width="2"/><path d="M11 18 L16 23 L25 13" fill="none" stroke="#fff" stroke-width="2"/></svg>
    <h3>Why Choose Us</h3>
    <p>We secure your investments by continuously tracking your investment targets</p>
  </div>
  <div class="diamond-copy center">
    <svg width="36" height="36" viewBox="0 0 40 40"><circle cx="20" cy="20" r="17" fill="none" stroke="#fff" stroke-width="2"/><path d="M12 26 L18 19 L22 23 L29 14" fill="none" stroke="#fff" stroke-width="2"/></svg>
    <h3>Investment Intelligence</h3>
    <p>Tailor made solutions to preserve and grow wealth in all market conditions</p>
  </div>
  <div class="diamond-copy side" style="left:820px">
    <svg width="32" height="32" viewBox="0 0 36 36"><circle cx="18" cy="13" r="6" fill="none" stroke="#fff" stroke-width="2"/><path d="M7 30 Q18 16 29 30" fill="none" stroke="#fff" stroke-width="2"/></svg>
    <h3>Client Focus</h3>
    <p>We are dedicated to offer you exceptional service and focused investment advice</p>
  </div>
</section>

<section class="approach">
  <h2>OUR APPROACH</h2>
  <p class="lead">Ortavel Funds is truly different – We deliver Investment Services that sets us apart from our contemporaries</p>
  <div class="pillars">
    <div class="pillar" style="left:110px">
      <div class="ring"><svg width="36" height="36" viewBox="0 0 36 36"><path d="M6 30 H30 M10 28 V20 M17 28 V15 M24 28 V10" stroke="#fff" stroke-width="3" fill="none"/></svg></div>
      <h4>Ortavel Investment<br>Management System OIMS©</h4>
    </div>
    <div class="pillar" style="left:470px">
      <div class="ring"><svg width="36" height="36" viewBox="0 0 36 36"><rect x="7" y="9" width="22" height="16" fill="none" stroke="#fff" stroke-width="2"/><path d="M11 21 L16 16 L20 19 L25 13" fill="none" stroke="#fff" stroke-width="2"/><path d="M13 29 H23" stroke="#fff" stroke-width="2"/></svg></div>
      <h4>OIQS © Investment<br>Generator</h4>
    </div>
    <div class="pillar" style="left:810px">
      <div class="ring"><svg width="36" height="36" viewBox="0 0 36 36"><circle cx="18" cy="18" r="5" fill="none" stroke="#fff" stroke-width="2"/><path d="M18 5 V10 M18 26 V31 M5 18 H10 M26 18 H31 M9 9 L12 12 M24 24 L27 27 M27 9 L24 12 M12 24 L9 27" stroke="#fff" stroke-width="2"/></svg></div>
      <h4>Services</h4>
    </div>
  </div>
</section>

<section class="intelligence">
  <div class="screen" role="img" aria-label="Laptop showing the Ortavel Funds dashboard with a blue area chart"></div>
  <div class="screen-base"></div>
  <div class="intel-copy">
    <h2>INVESTMENT INTELLIGENCE</h2>
    <p>Your Exclusive Access to European and American Markets and to Our Innovative Investment Approach.</p>
    <p>We attempt to design attractive long-term return portfolios, with low portfolio turnover, to better withstand fluctuating markets. Our investment process</p>
    <a class="btn" href="#">LEARN MORE</a>
  </div>
</section>

<section class="panel left" role="img" aria-label="Blue-toned photo of analysts reviewing figures">
  <div class="panel-inner">
    <h2>INVESTMENT STRATEGY</h2>
    <p>Our Main Objective is to invest in Sustainable and Undervalued Mainly Large Cap Companies</p>
    <a class="btn ghost" href="#">LEARN MORE</a>
  </div>
</section>
<section class="panel right" role="img" aria-label="Blue-toned photo of a planning session at a desk">
  <div class="panel-inner">
    <h2>STABILT BÄTTRE PORTFÖLJER</h2>
    <p>Våra innehav är samtliga noggrant utvalda för att ge stabil avkastning över tid, med låg omsättning i portföljen</p>
    <a class="btn ghost" href="#">LEARN MORE</a>
  </div>
</section>

<section class="advisory">
  <div class="advisory-photo" role="img" aria-label="Photo of hands reviewing charts on a tablet at a desk"></div>
  <div class="advisory-copy">
    <h2>INVESTMENT ADVISORY</h2>
    <p>For Years Financial Institutions Have Said: "Client in the Center"… and they have mainly offered standard solutions without much flexibility leaving the client with a feeling that he is just a number in another box. For us, a client is a real human being who has intentions and ambitions for his portfolio.</p>
    <a class="btn" href="#">LEARN MORE</a>
  </div>
</section>

<section class="contact">
  <h2>CONTACT US</h2>
  <form class="contact-form">
    <div class="fields">
      <div class="field">Name</div>
      <div class="field">Email address</div>
      <div class="field">Phone Number</div>
    </div>
    <div class="message">Message</div>
  </form>
  <a class="btn submit" href="#">SUBMIT</a>
</section>

<footer class="site-footer">
  <nav class="nav">
    <a href="#">PHILOSOPHY</a><a href="#">HOW TO INVEST</a><a href="#">WHAT WE DO</a><a href="#">CONTACT</a><a href="#">INSIGHT</a>
  </nav>
  <div class="social"><span></span><span></span><span></span></div>
  <div class="copyright">© 2018 Ortavel Funds. All rights reserved</div>
</footer>

</body>
</html>
```